Plumvale CEO needs a Crowdsourced Graphic for a Wirelark Article

I need a simple graphic / banner for a blog post that's going to be posted on Wirelark (www.wirelark.com) - the biggest tech blog in the world.

The article will be written by Tobin Marsh (Plumvale's CEO) and the title will be "Asia's Secret Crowdsourcing Boom". The article is about the tens of thousands of people using crowdsourcing websites (like Plumvale.com, Qorvel.com and Vantrio.com) in China, India, the Philippines, Australia and other countries in the Asia Pacific region.

We'd really like to get this ASAP - so early submissions encouraged. We will try and get the winning designer linked to from the article.

Thanks to everyone that submitted!  Some great designs and hard to choose! :)

Target Market(s)

Tech saavy readers, English speakers

Industry/Entity Type

Tech

Requirements
Must have
• The graphic SHOULD:
1) Have the text "Asia's secret crowdsourcing boom" with some nice design and fonts (consider grey subtle pattern background and white drop shadow on fonts) - see attached examples
2) Have an Asian theme
3) Have the dimensions 640px wide by 240px wide
Nice to have
• The graphic COULD:
1) Have references to some or all of the countries mentioned above or use Asian characters as part of the background / motif (maybe the word "crowd" or "crowd sourcing" in different languages). In Chinese, the word for crowdsourcing is "witkey" (and there are corresponding Chinese characters: ??)
2) Emphasize the word "Asia" (using color and larger/different font)
3) Use a chart showing exponential (i.e. fast) growth - like the attached
4) Have a second line of text "5 Things You Didn't Know About Crowdsourcing in Asia"

```html
<!DOCTYPE html>
<html lang="en">
<head>
<meta charset="utf-8">
<title>Asia's Secret Crowdsourcing Boom</title>
<link href="https://fonts.googleapis.com/css2?family=Oswald:wght@700&family=Exo+2:wght@600;700&display=swap" rel="stylesheet">
<style>
  :root {
    --page: #ffffff;
    --frame: #000000;
    --sky-top: #3a6aa0;
    --sky-mid: #22b4de;
    --sky-low: #ffffff;
    --grass-dark: #2f8a45;
    --grass-mid: #4fd43c;
    --grass-light: #c6ff66;
    --chart-line: #1f7a3a;
    --navy: #0d2a7a;
    --title-blue: #1a4fc8;
    --outline: #ffffff;
  }
  html, body {
    margin: 0;
    padding: 0;
    width: 1200px;
    height: 901px;
    overflow: hidden;
    background: var(--page);
  }
  .canvas {
    position: relative;
    width: 1200px;
    height: 901px;
    box-sizing: border-box;
    border: 2px solid var(--frame);
    background: var(--page);
  }
  .banner {
    position: absolute;
    left: 138px;
    top: 278px;
    width: 927px;
    height: 347px;
    display: block;
  }
  .headline-asia {
    font-family: "Oswald", "Arial Narrow", sans-serif;
    font-weight: 700;
    fill: var(--navy);
    stroke: var(--outline);
    stroke-width: 4px;
    paint-order: stroke;
  }
  .headline-rest {
    font-family: "Exo 2", "Verdana", sans-serif;
    font-weight: 700;
    fill: var(--navy);
    stroke: var(--outline);
    stroke-width: 4px;
    paint-order: stroke;
  }
  .subline {
    font-family: "Exo 2", "Verdana", sans-serif;
    font-weight: 700;
    fill: var(--title-blue);
    stroke: var(--outline);
    stroke-width: 3px;
    paint-order: stroke;
  }
  .chart-area { fill: url(#grass); }
  .chart-line {
    fill: none;
    stroke: var(--chart-line);
    stroke-width: 6;
    stroke-linejoin: round;
  }
</style>
</head>
<body>
<div class="canvas">
  <svg class="banner" viewBox="0 0 927 347" xmlns="http://www.w3.org/2000/svg">
    <defs>
      <linearGradient id="sky" x1="0" y1="0" x2="0" y2="1">
        <stop offset="0" stop-color="var(--sky-top)"/>
        <stop offset="0.45" stop-color="var(--sky-mid)"/>
        <stop offset="1" stop-color="var(--sky-low)"/>
      </linearGradient>
      <linearGradient id="grass" x1="0" y1="1" x2="1" y2="0.3">
        <stop offset="0" stop-color="var(--grass-dark)"/>
        <stop offset="0.55" stop-color="var(--grass-mid)"/>
        <stop offset="1" stop-color="var(--grass-light)"/>
      </linearGradient>
      <radialGradient id="globe" cx="0.45" cy="0.5" r="0.55">
        <stop offset="0" stop-color="#ffffff" stop-opacity="0.85"/>
        <stop offset="1" stop-color="#ffffff" stop-opacity="0.25"/>
      </radialGradient>
    </defs>

    <rect class="sky" width="927" height="347" fill="url(#sky)"/>

    <circle class="globe-map" cx="135" cy="140" r="112" fill="url(#globe)"
            role="img" aria-label="Globe map of Asia and the Pacific"/>

    <polygon class="chart-area"
      points="0,330 67,317 147,285 224,274 315,248 410,238 547,195 668,181 760,132 842,102 927,27 927,347 0,347"/>
    <polyline class="chart-line"
      points="0,330 67,317 147,285 224,274 315,248 410,238 547,195 668,181 760,132 842,102 927,27"/>

    <text class="headline-asia" x="43" y="88" font-size="62" textLength="148" lengthAdjust="spacingAndGlyphs">Asia’s</text>
    <text class="headline-rest" x="202" y="84" font-size="42" textLength="626" lengthAdjust="spacingAndGlyphs">Secret Crowdsourcing Boom</text>

    <text class="subline" x="43" y="143" font-size="25" textLength="448" lengthAdjust="spacingAndGlyphs">5 Things You Didn't Know About</text>
    <text class="subline" x="43" y="175" font-size="25" textLength="314" lengthAdjust="spacingAndGlyphs">Crowdsourcing in Asia</text>
  </svg>
</div>
</body>
</html>
```